Gaming "Ember Tonic" Energy Drink CAN Design

Energy Drink called "Ember Tonic" which should include the classic Health Potions out of a video game like, Morvath, Realm of Ironvale, Crystal Odyssey, Stone Banners, Towers and Tempests and so on. Our Products is focused on gamers, geeks and nerds. DESIGN INFORMATION We want to have a design that fits the style of health potions we are looking for of a video game. The main color should be RED, which is the usual color for a Ember Tonic in a video game. The word "Ember Tonic" has become to be visible on the product foremost.
Updates

Langsam um Feedback zu geben

Target Market(s)

Gamers geeks and nerds

Font styles to use
Serif
Sans Serif
Decorative
Script

Colors
ec1f27

Requirements
Must have
• The Color Red has to be dominant, as the Ember Tonic is in a Video Game is Red
Nice to have
• Something that resembles a Ember Tonic out of a game like: Morvath, Realm of Ironvale, Crystal Odyssey

```html
<!DOCTYPE html>
<html lang="de">
<head>
<meta charset="utf-8">
<title>Ember Tonic – Dosenetikett</title>
<link href="https://fonts.googleapis.com/css2?family=Cinzel:wght@700&family=Open+Sans:wght@400;600;700&display=swap" rel="stylesheet">
<style>
  :root {
    --page: #1d2430;
    --black: #1a1a1a;
    --red: #ec1f27;
    --gold: #c9a233;
    --gold-light: #e6c65a;
    --rope: #8a5a2b;
    --parchment: #efe6cf;
    --ink: #2b2620;
  }
  * { box-sizing: border-box; margin: 0; padding: 0; }
  html, body { width: 1200px; height: 803px; overflow: hidden; background: var(--page); }
  .canvas {
    width: 1200px; height: 803px;
    display: flex; align-items: center; justify-content: center;
  }
  .label {
    width: 820px; height: 600px;
    display: grid; grid-template-rows: 70px 30px 1fr 30px 40px;
    border-radius: 6px; overflow: hidden;
    box-shadow: 0 20px 50px rgba(0,0,0,.5);
  }
  .band-top { background: var(--black); }
  .band-rope { background: linear-gradient(var(--rope), #5e3a19 50%, var(--rope)); }
  .band-base { background: var(--gold); }
  .body {
    background: var(--red);
    display: grid; grid-template-columns: 1fr 1fr;
    min-height: 0;
  }
  .front {
    display: flex; flex-direction: column; align-items: center; justify-content: center;
    gap: 22px; padding: 20px;
  }
  .shield {
    width: 300px; height: 220px;
    display: flex; align-items: center; justify-content: center;
    background: var(--black);
    border: 6px solid var(--gold);
    border-radius: 14px 14px 120px 120px;
  }
  .product-name {
    font-family: "Cinzel", serif; font-weight: 700;
    color: var(--gold-light);
    font-size: 46px; line-height: 1.05; text-align: center;
  }
  .brand {
    display: flex; align-items: center; gap: 10px;
    font-family: "Open Sans", sans-serif; font-weight: 600;
    font-size: 22px; color: var(--parchment);
  }
  .brand-mark { width: 14px; height: 14px; background: var(--parchment); }
  .back { padding: 14px 30px; display: flex; min-height: 0; }
  .info-panel {
    flex: 1;
    background: var(--parchment);
    border: 2px solid #8b6b3a;
    padding: 10px 14px;
    font-family: "Open Sans", sans-serif; font-size: 8px; line-height: 1.3;
    color: var(--ink); text-transform: uppercase;
    display: flex; flex-direction: column; gap: 6px;
  }
  .nutrition { width: 100%; border: 1px solid var(--ink); border-collapse: collapse; }
  .nutrition td { padding: 1px 5px; }
  .nutrition td:last-child, .nutrition td.num { text-align: right; }
  .nutrition .section td { padding-top: 4px; }
  .info-foot { display: flex; gap: 10px; margin-top: auto; }
  .info-foot .notes { flex: 1; }
  .code-box { width: 70px; background: #d8d8d8; position: relative; }
  .volume {
    position: absolute; bottom: 4px; right: 4px;
    font-size: 12px; font-weight: 700; text-transform: none;
  }
</style>
</head>
<body>
<main class="canvas">
  <section class="label">
    <div class="band-top"></div>
    <div class="band-rope" role="img" aria-label="Gedrehtes Seil als Zierband"></div>
    <div class="body">
      <div class="front">
        <div class="shield">
          <h1 class="product-name">Ember<br>Tonic</h1>
        </div>
        <div class="brand"><span class="brand-mark"></span>Questbrew</div>
      </div>
      <div class="back">
        <div class="info-panel">
          <p>Energy Drink – pfandfrei<br>
          Erhöhter Koffeingehalt (32mg/100ml)<br>
          Zutaten: Molkenerzeugnis*, Wasser, Zucker, Säuerungsmittel E330, Kohlensäure, Säureregulatoren: E331, E332; Karamellisierter Zucker, Aroma, Glukuronolakton (0,04%), Taurin (0,4%), Koffein (0,03%), Inosit (0,02%), Vitamine: Niacin, Pantothensäure, Vitamin B6, Vitamin B12; Farbstoffe: E150d, E101</p>
          <table class="nutrition">
            <tr><td>Nährwerte</td><td></td><td>in 100ml</td></tr>
            <tr><td>Brennwert</td><td></td><td>198 kJ / 47 kcal</td></tr>
            <tr><td>Fett</td><td></td><td>0 g</td></tr>
            <tr><td>&nbsp;davon gesättigte Fettsäuren</td><td></td><td>0 g</td></tr>
            <tr><td>Kohlenhydrate</td><td></td><td>11,1 g</td></tr>
            <tr><td>&nbsp;davon Zucker</td><td></td><td>10,9 g</td></tr>
            <tr><td>Eiweiss</td><td></td><td>0 g</td></tr>
            <tr><td>Salz</td><td></td><td>&lt; 0,1 g</td></tr>
            <tr class="section"><td>Vitamine</td><td class="num">in 100ml</td><td>% NRV**</td></tr>
            <tr><td>Niacin</td><td class="num">7,04 mg</td><td>44%</td></tr>
            <tr><td>Vitamin B6</td><td class="num">1,4 mg</td><td>100%</td></tr>
            <tr><td>Vitamin B12</td><td class="num">5,0 µg</td><td>200%</td></tr>
            <tr><td>Pantothensäure</td><td class="num">1,98 mg</td><td>33%</td></tr>
          </table>
          <p>* Enthält ein Milcherzeugnis<br>** der Nährstoffbezugswerte</p>
          <div class="info-foot">
            <p class="notes">Gekühlt trinken. Pasteurisiert.<br>
            In moderaten Mengen konsumieren. Für Kinder und schwangere oder stillende Frauen nicht empfohlen.<br>
            Hergestellt in Österreich von Kettleforge Production &amp; Development GmbH<br>
            Brauweg 12, 4020 Linz<br>
            Mindestens haltbar bis: siehe Dosenboden</p>
            <div class="code-box"><span class="volume">℮ 250ml</span></div>
          </div>
        </div>
      </div>
    </div>
    <div class="band-rope" role="img" aria-label="Gedrehtes Seil als Zierband"></div>
    <div class="band-base"></div>
  </section>
</main>
</body>
</html>
```